KRL Going Cashless

Hello,
We are a medical office looking to get a flyer created to promote to our patients we will be going "Cashless." Our tagline will be "Cash-Less is Stress-Less"

"Starting in July, to offer you the fastest and most convenient service, we are transitioning to a cashless system. You can now enjoy faster checkout times and greater security with card and contactless payments. More info to come."

I've added two other flyers as sample designs we've used.

Please include logo, addresses, website, phone number

Files to include jpeg, png, pdf (under 5mb), Facebook and Instagram sizing.

Thank you,
Doran

```html
<!DOCTYPE html>
<html lang="en">
<head>
<meta charset="utf-8">
<title>KRL Going Cashless</title>
<link rel="stylesheet" href="https://fonts.googleapis.com/css2?family=Anton&family=Oswald:wght@500&family=Open+Sans:wght@600&family=Roboto+Slab:wght@500;700&display=swap">
<style>
  :root {
    --page: #e6e6e6;
    --ink: #27232b;
    --orange: #f27f42;
    --teal: #5cc6ab;
    --cream: #fdf1e7;
    --peach: #fcd2b4;
    --sky: #d9e4ec;
    --warm: #e9d3c2;
    --white: #ffffff;
  }
  * { margin: 0; padding: 0; box-sizing: border-box; }
  html, body { width: 1200px; height: 638px; overflow: hidden; background: var(--page); }
  .flyer {
    position: absolute; left: 367px; top: 19px; width: 465px; height: 600px;
    overflow: hidden; color: var(--ink);
    box-shadow: 0 6px 18px rgba(0,0,0,.18);
  }
  .hero-photo {
    position: absolute; inset: 0;
    background: linear-gradient(100deg, var(--sky) 0%, #e4e6e6 40%, var(--warm) 62%, #b39a7e 80%, #8d8a6a 100%);
  }
  .shapes { position: absolute; inset: 0; }
  .headline {
    position: absolute; left: 30px; top: 28px;
    font: 62px/1 "Anton", sans-serif; letter-spacing: .5px;
  }
  .tagline {
    position: absolute; left: 30px; top: 110px; width: 189px; height: 43px;
    background: var(--orange); color: var(--white);
    font: 600 14px/17px "Open Sans", sans-serif; padding: 5px 6px;
  }
  .phone {
    position: absolute; left: 30px; top: 172px;
    font: 500 33px/1 "Oswald", sans-serif;
  }
  .web {
    position: absolute; left: 30px; top: 216px;
    font: 700 12.5px/1 "Roboto Slab", serif; letter-spacing: 1.4px;
  }
  .badge {
    position: absolute; left: 20px; top: 248px; width: 204px; height: 204px;
    border-radius: 50%; background: var(--orange); border: 7px solid var(--cream);
    text-align: center; padding-top: 42px;
  }
  .badge-title { font: 29px/34px "Anton", sans-serif; }
  .badge-rule { width: 150px; height: 1px; background: var(--cream); margin: 6px auto 7px; }
  .badge-sub { font: 500 16.5px/19px "Oswald", sans-serif; }
  .foot-photo {
    position: absolute; left: 172px; top: 389px; width: 138px; height: 138px;
    border-radius: 50%; border: 5px solid var(--cream);
    background: radial-gradient(circle at 55% 55%, #f1d7c6 0%, #e6e3e2 45%, #9fb0b4 100%);
  }
  .notice {
    position: absolute; left: 312px; top: 352px; width: 148px; text-align: center;
  }
  .notice-title { font: 700 15.5px/19px "Roboto Slab", serif; }
  .notice-body { font: 500 10.5px/13.5px "Roboto Slab", serif; margin-top: 4px; }
  .notice-small { font: 500 8.5px/11px "Roboto Slab", serif; margin-top: 5px; padding: 0 6px; }
  .address {
    position: absolute; left: 325px; top: 512px; width: 107px; height: 75px;
    background: var(--peach); text-align: center; padding: 5px 6px 0;
    font: normal 500 9px/11.5px "Roboto Slab", serif;
  }
  .address-lead { font: 700 10px/13px "Roboto Slab", serif; margin-bottom: 2px; }
  .brand {
    position: absolute; left: 30px; top: 556px;
    font: 700 17px/1 "Roboto Slab", serif; color: var(--cream);
    letter-spacing: .3px;
  }
</style>
</head>
<body>
  <article class="flyer">
    <div class="hero-photo" role="img" aria-label="Photo of a smiling woman with long curly hair looking at her phone"></div>

    <svg class="shapes" viewBox="0 0 465 600" width="465" height="600" aria-hidden="true">
      <polygon points="0,345 190,440 356,600 0,600" fill="var(--ink)"/>
      <polygon points="465,268 465,600 356,600 185,445 215,410" fill="var(--teal)"/>
      <polygon points="465,254 465,268 215,410 196,412" fill="var(--orange)"/>
    </svg>

    <h1 class="headline">CASHLESS</h1>
    <p class="tagline">TAKE CARE OF YOUR<br>FOOT AND ANKLE NOW</p>
    <p class="phone">(555)214-0386</p>
    <p class="web">www.stridewellcare.com</p>

    <div class="badge">
      <p class="badge-title">CASH-LESS IS<br>STRESS-LESS</p>
      <div class="badge-rule"></div>
      <p class="badge-sub">FOOT &amp; ANKLE<br>SPECIALISTS</p>
    </div>

    <div class="foot-photo" role="img" aria-label="Photo of a doctor in gloves examining a patient's foot"></div>

    <section class="notice">
      <h2 class="notice-title">STARTING IN<br>JULY,</h2>
      <p class="notice-body">to offer you the fastest and most convenient service, we are transitioning to a cashless system.</p>
      <p class="notice-small">You can now enjoy faster checkout times and greater security with card and contactless payments.</p>
    </section>

    <address class="address">
      <p class="address-lead">More info to come.</p>
      58 Linden Park Rd., Ste 210, Millbrook, MD 21040
    </address>

    <p class="brand">KRL Foot Care</p>
  </article>
</body>
</html>
```